Eco-friendly printer cartridges and toners packaging

Dear designers,

we are looking for a new packaging design for remanufactured printer consumables products. The design should clearly communicate ecology and economy (check inspirations attached - we like them :) ). To understand the ecological impact you can watch the presentation at http://www.verdaplix.sk/ecology.html . You can find also more information about the brand at http://www.verdaplix.sk/index1.html .

We currently need universal design for following sizes of product:

cartridges:

1. 60x25x90 mm
2. 60x45x90 mm
3. 80x45x120 mm

laser toners:

4. 178x110x345 mm

They all should be recoginezed at the first sight, that it is the same brand and by buying this product the customer contributes to saving enviroment and supports socially responsible company, while it also saves his/hers money.

The final packaging will be in blister.

And be as creative as possible. Its all up to you.

Feel free to ask as many questions as needed.

You do not have to stick to the packaging design and sizes in the attachement. The only thing you need to stick to is the actual product measures.

Reason: As we have a little more time than we expected, we postpone the deadline. We also have a lot of accepted project invitations and we are expecting the delivery. Thank you for understanding. Radim

Target Market(s)

Anyone who buys printer consumables. It should attract everyone who thinks ecologically and wants to save some money

Industry/Entity Type

It Company

Requirements
Must have
• 1. logo - will be attached (if you dont like current logo you can try to design new one)
2. ecological messages - up to you
3. Slovak and English manual - will be attached
4. Pictograms - will be attached (can be redisigned)
5. Compatibility - which printers is the cartridge/toner compatible with (blank space to be filled in)
6. Slovak and English copyright disclaimer - will be attached
7. Colour identification (black, cyan, magenta....)
8. ISO 9001 / ISO 14001
9. Made in Europe
10. Production Date
11. Part no.
12. Use before text - will be attached
Nice to have
• 1.we are currently remanufacturing cartridges and toners for printers of 12 different brands (dovrent, zq, bivot, murly...) The packaging should be somehow differentiated for each different brand (either by colour / it can be different colour of some line, or the whole backgroud or just some spot on the packaging/, different fruit on the packaging, or whatever you consider to be the best option.

2. nature in the design

```html
<!DOCTYPE html>
<html lang="en">
<head>
<meta charset="utf-8">
<title>RubiTone Toner Box Dieline</title>
<link rel="stylesheet" href="https://fonts.googleapis.com/css2?family=Open+Sans:wght@400;600;700;800&family=Didact+Gothic&display=swap">
<style>
  :root {
    --box-red: #b9252f;
    --deep-red: #8e1a22;
    --paper: #ffffff;
    --ink: #1d1d1b;
    --cut-line: #2b2b2b;
    --fold-line: #7f93ad;
    --tuck-line: #2aa7b3;
    --peach: #f4b9a3;
    --pink-text: #f6c9cf;
    --soft-grey: #6d6d6d;
    --eco-green: #7ba63b;
    --eco-ring: #c9dca6;
  }
  html, body {
    margin: 0;
    padding: 0;
    width: 1200px;
    height: 1200px;
    overflow: hidden;
    background: var(--paper);
  }
  .dieline {
    display: block;
    width: 1200px;
    height: 1200px;
  }
  .panel-red { fill: var(--box-red); }
  .panel-white { fill: var(--paper); }
  .cut { fill: none; stroke: var(--cut-line); stroke-width: 0.9; }
  .fold { fill: none; stroke: var(--fold-line); stroke-width: 1.1; stroke-dasharray: 4 3; }
  .tuck-fold { fill: none; stroke: var(--tuck-line); stroke-width: 1.1; stroke-dasharray: 4 3; }
  .hang-slot { fill: var(--paper); }
  .copy-area {
    font-family: "Didact Gothic", sans-serif;
    font-size: 21px;
    letter-spacing: 1px;
    fill: var(--ink);
  }
  .brand-name { font-family: "Open Sans", sans-serif; font-weight: 800; fill: var(--ink); }
  .subline { font-family: "Open Sans", sans-serif; font-weight: 400; }
  .sub-grey { fill: var(--soft-grey); }
  .sub-pink { fill: var(--pink-text); }
  .sub-deep { fill: var(--deep-red); }
  .part-no { font-family: "Open Sans", sans-serif; font-weight: 800; }
  .part-red { fill: var(--box-red); }
  .part-dark { fill: var(--ink); }
  .part-white { fill: var(--paper); }
  .product-name { font-family: "Open Sans", sans-serif; font-weight: 700; fill: var(--peach); }
  .eco-badge { fill: var(--eco-green); stroke: var(--eco-ring); stroke-width: 2; }
</style>
</head>
<body>
<svg class="dieline" viewBox="0 0 750 750" xmlns="http://www.w3.org/2000/svg">
  <defs>
    <linearGradient id="ink-strokes" x1="0" y1="0" x2="1" y2="0">
      <stop offset="0" stop-color="#1f1f1f"/>
      <stop offset="0.3" stop-color="#e4b737"/>
      <stop offset="0.6" stop-color="#c8242e"/>
      <stop offset="1" stop-color="#2767a8"/>
    </linearGradient>
  </defs>

  <!-- Glue flap -->
  <path class="panel-white cut" d="M66,228 L18,240 L18,568 L66,580"/>

  <!-- Back panel with hanger -->
  <g class="back-panel">
    <path class="panel-white cut" d="M70,67 L74,32 Q75,25 82,25 L283,25 Q290,25 291,32 L296,67"/>
    <rect class="panel-red" x="66" y="67" width="234" height="513"/>
    <path class="cut" d="M300,152 L300,200 L292,210 L292,222 L300,228"/>
    <path class="hang-slot" d="M132,98 L165,98 Q172,90 183,90 Q194,90 200,98 L234,98 Q245,98 245,110 Q245,122 234,122 L200,122 Q194,130 183,130 Q172,130 165,122 L132,122 Q120,122 120,110 Q120,98 132,98 Z"/>
    <path class="hang-slot" d="M132,178 L165,178 Q172,170 183,170 Q194,170 200,178 L234,178 Q245,178 245,190 Q245,202 234,202 L200,202 Q194,210 183,210 Q172,210 165,202 L132,202 Q120,202 120,190 Q120,178 132,178 Z"/>
    <text class="copy-area" x="182" y="370" text-anchor="middle">COPY</text>
    <text class="copy-area" x="182" y="397" text-anchor="middle">AREA</text>
  </g>

  <!-- Left side panel -->
  <g class="side-panel-left">
    <rect class="panel-red" x="300" y="152" width="100" height="508"/>
    <path class="cut" d="M303,228 L314,170 L390,162 L397,228"/>
    <path class="cut" d="M303,580 L314,640 L390,648 L397,580"/>
    <text class="copy-area" transform="translate(352,400) rotate(-90)" text-anchor="middle">COPY  AREA</text>
    <circle class="eco-badge" cx="350" cy="548" r="28"/>
  </g>

  <!-- Front panel -->
  <g class="front-panel">
    <path class="panel-white cut" d="M400,135 L400,108 Q400,85 430,85 L605,85 Q635,85 635,108 L635,135"/>
    <rect class="panel-white" x="400" y="130" width="235" height="278"/>
    <rect role="img" aria-label="Illustration of four ink brush strokes in black, yellow, red and blue" x="400" y="228" width="235" height="180" fill="url(#ink-strokes)"/>
    <rect class="panel-red" x="400" y="408" width="235" height="247"/>

    <text class="brand-name" x="410" y="165" font-size="21">RubiTone</text>
    <text class="subline sub-grey" x="411" y="180" font-size="11.5">Ink Jet Printer Toner</text>
    <text class="subline sub-grey" x="411" y="194" font-size="11.5">for Bivot 530</text>
    <text class="part-no part-red" x="410" y="220" font-size="20">#0000</text>

    <text class="product-name" x="411" y="452" font-size="24">Product NAME</text>
    <text class="brand-name" x="410" y="490" font-size="40">RubiTone</text>
    <text class="subline sub-pink" x="410" y="515" font-size="19">Ink Jet Printer Toner</text>
    <text class="subline sub-pink" x="623" y="540" font-size="19" text-anchor="end">for Bivot 530</text>
    <text class="part-no part-dark" x="618" y="570" font-size="20" text-anchor="end">#0000</text>
    <circle class="eco-badge" cx="435" cy="548" r="28"/>

    <text class="brand-name" x="410" y="622" font-size="23">RubiTone</text>
    <text class="subline sub-deep" x="411" y="637" font-size="11.5">Ink Jet Printer Toner</text>
    <text class="subline sub-deep" x="411" y="650" font-size="11.5">for Bivot 530</text>
    <text class="part-no part-white" x="632" y="653" font-size="16" text-anchor="end">#0000</text>

    <path class="panel-white cut" d="M400,655 L400,688 Q400,725 440,725 L595,725 Q635,725 635,688 L635,655"/>
    <path class="cut" d="M400,128 L400,655 M635,128 L635,655"/>
  </g>

  <!-- Right side panel -->
  <g class="side-panel-right">
    <rect class="panel-red" x="635" y="152" width="85" height="508"/>
    <path class="cut" d="M638,228 L647,170 L712,162 L717,228"/>
    <path class="cut" d="M638,580 L647,640 L712,648 L717,580"/>
    <text class="copy-area" transform="translate(672,405) rotate(90)" text-anchor="middle">COPY  AREA</text>
    <circle class="eco-badge" cx="680" cy="548" r="28"/>
  </g>

  <!-- Fold lines -->
  <g class="folds">
    <line class="fold" x1="66" y1="75" x2="300" y2="75"/>
    <line class="fold" x1="66" y1="152" x2="300" y2="152"/>
    <line class="fold" x1="66" y1="228" x2="720" y2="228"/>
    <line class="fold" x1="66" y1="580" x2="720" y2="580"/>
    <line class="fold" x1="66" y1="228" x2="66" y2="580"/>
    <line class="fold" x1="300" y1="228" x2="300" y2="580"/>
    <line class="fold" x1="400" y1="228" x2="400" y2="580"/>
    <line class="fold" x1="635" y1="228" x2="635" y2="580"/>
    <line class="tuck-fold" x1="400" y1="135" x2="635" y2="135"/>
    <line class="fold" x1="400" y1="655" x2="635" y2="655"/>
  </g>
</svg>
</body>
</html>
```